Business Card Design for Small Electrical Contractor

I need to update my business card into something a little more modern. We are a small electrical contracting company. We service domestic and commercial places around Sydney. We have 2 logo designs at the moment. I have uploaded both and 2 different sizes to work with.

Industry/Entity Type

Business

Contact Information for Business Card

Leo Hartigan
8/21-23 Birch Rd, Kelsworth 2087
t - (02) 9381 4720
m - 0427 815 903
E - info@hartiganelx.com.au
W - hartiganelx.com.au
ABN: 42 907 551 316

Font styles to use
Sans Serif

Requirements
Must have
• I would also like to see the below fit on somewhere aswell
• - Licensed Electrician
• - Level 2 (Cat 1 & 4)
• - Domestic
• - Commercial
• - Repairs and Installations
• - Data
Nice to have
• Try and keep similar colours as logo
Should not have
• No lightning bolts or light globes. Smart and professional please.

```html
<!DOCTYPE html>
<html lang="en">
<head>
<meta charset="utf-8">
<title>L&amp;J Hartigan Electrical – Business Card</title>
<link rel="stylesheet" href="https://fonts.googleapis.com/css2?family=Lato:wght@400;700&display=swap">
<style>
  :root {
    --green: #12353a;
    --orange: #f7941d;
    --white: #ffffff;
    --ink: #1d2b2e;
    --backdrop: #e4e4e4;
  }
  * { margin: 0; padding: 0; box-sizing: border-box; }
  html, body { width: 1200px; height: 680px; overflow: hidden; }
  body {
    background: var(--backdrop);
    font-family: "Lato", Arial, sans-serif;
    position: relative;
  }
  .card {
    position: absolute;
    top: 185px;
    width: 540px;
    height: 310px;
    overflow: hidden;
    box-shadow: 0 6px 18px rgba(0,0,0,0.18);
  }
  .card-front { left: 40px; background: var(--white); }
  .card-back { left: 620px; background: var(--green); }

  .front-wave { position: absolute; inset: 0; }

  .brand-name {
    font-weight: 700;
    letter-spacing: 0.5px;
    line-height: 1.15;
  }
  .card-front .brand-name {
    position: absolute;
    left: 30px;
    top: 105px;
    width: 250px;
    font-size: 26px;
    color: var(--green);
  }
  .divider {
    position: absolute;
    left: 300px;
    top: 40px;
    width: 1px;
    height: 150px;
    background: #bfc6c7;
  }
  .contact {
    position: absolute;
    left: 320px;
    top: 38px;
    color: var(--ink);
    font-size: 13px;
    line-height: 1.35;
  }
  .contact-name { font-size: 17px; }
  .contact-role { font-size: 13px; margin-bottom: 10px; }
  .contact-address { margin-bottom: 6px; }
  .contact-line { display: flex; align-items: center; gap: 8px; }
  .contact-line svg { width: 11px; height: 11px; fill: var(--ink); flex: none; }
  .website {
    position: absolute;
    left: 0;
    right: 0;
    bottom: 14px;
    text-align: center;
    color: var(--white);
    font-size: 14px;
    letter-spacing: 0.6px;
  }

  .card-back .brand-name {
    position: absolute;
    left: 50px;
    top: 70px;
    width: 440px;
    font-size: 38px;
    color: var(--white);
  }
  .brand-rule {
    position: absolute;
    left: 50px;
    top: 165px;
    width: 300px;
    height: 2px;
    background: var(--orange);
  }
  .services {
    position: absolute;
    left: 50px;
    top: 195px;
    width: 440px;
    color: var(--white);
    font-size: 15px;
    line-height: 1.5;
    letter-spacing: 0.3px;
  }
  .services .dot { color: var(--orange); padding: 0 4px; }
</style>
</head>
<body>

<section class="card card-front">
  <svg class="front-wave" viewBox="0 0 540 310" preserveAspectRatio="none" aria-hidden="true">
    <path d="M0,288 Q300,266 540,132 L540,142 Q300,274 0,292 Z" fill="var(--orange)"/>
    <path d="M0,298 Q300,284 540,152 L540,310 L0,310 Z" fill="var(--green)"/>
  </svg>

  <div class="brand-name">L&amp;J Hartigan Electrical</div>

  <div class="divider"></div>

  <div class="contact">
    <div class="contact-name">Leo Hartigan</div>
    <div class="contact-role">Owner</div>
    <div class="contact-address">8/21-23 Birch Rd<br>Kelsworth 2087</div>
    <div class="contact-line">
      <svg viewBox="0 0 24 24"><path d="M6.6 10.8a15.1 15.1 0 0 0 6.6 6.6l2.2-2.2a1 1 0 0 1 1-.25 11.4 11.4 0 0 0 3.6.57 1 1 0 0 1 1 1V20a1 1 0 0 1-1 1A17 17 0 0 1 3 4a1 1 0 0 1 1-1h3.5a1 1 0 0 1 1 1c0 1.25.2 2.45.57 3.57a1 1 0 0 1-.25 1z"/></svg>
      <span>(02) 9381 4720</span>
    </div>
    <div class="contact-line">
      <svg viewBox="0 0 24 24"><rect x="6" y="1" width="12" height="22" rx="2"/><rect x="8" y="4" width="8" height="13" fill="#fff"/></svg>
      <span>0427 815 903</span>
    </div>
    <div class="contact-line">
      <svg viewBox="0 0 24 24"><path d="M2 5h20v14H2z"/><path d="M2 5l10 8 10-8" fill="none" stroke="#fff" stroke-width="2"/></svg>
      <span>info@hartiganelx.com.au</span>
    </div>
  </div>

  <div class="website">www.hartiganelx.com.au</div>
</section>

<section class="card card-back">
  <div class="brand-name">L&amp;J Hartigan Electrical</div>
  <div class="brand-rule"></div>
  <p class="services">
    Licensed Electrician<span class="dot">•</span>Level 2 (Cat 1 &amp; 4)<span class="dot">•</span>Domestic<br>
    Commercial<span class="dot">•</span>Repairs and Installations<span class="dot">•</span>Data
  </p>
</section>

</body>
</html>
```